Business card design for Automotive workshop

We need a business card for a new automotive repair and tyre shop called Ridgeback Prime Automotive located in New Zealand. We are a clean, modern and fresh workshop and company.

Front needs to feature logo,
my name:
Lachie Westergaard (director)

Address:
48 Marlow Lane
Whitianga 3510

Phone: 07 842 1937
Mobile: 027 519 2764
Email: office@ridgebackmotors.co.nz
Website: ridgebackmotors.co.nz

Back needs to feature an area to write down appointment details, date and time.

Also feature a list of jobs and work we do such as,
Vehicle Servicing
All Mechanical Repairs
Warrant of Fitness
Tyres & Wheel Alignments
Automotive Diagnostics
Automotive Parts & Supplies

```html
<!DOCTYPE html>
<html lang="en">
<head>
<meta charset="utf-8">
<title>Ridgeback Prime Automotive – Business Card</title>
<link rel="stylesheet" href="https://fonts.googleapis.com/css2?family=Bebas+Neue&family=Exo+2:wght@400;700&family=Montserrat:wght@500;700&display=swap">
<style>
  :root {
    --bg-dark: #4a5260;
    --bg-light: #8a9099;
    --card-dark: #3b3b3b;
    --card-white: #ffffff;
    --brand-red: #e3151f;
    --ink: #2b2b2b;
    --muted: #8b8b8b;
    --rule: #9a9a9a;
    --band-black: #050505;
  }
  * { box-sizing: border-box; margin: 0; padding: 0; }
  html, body { width: 1200px; height: 900px; overflow: hidden; }
  body {
    background: linear-gradient(90deg, var(--bg-dark), var(--bg-light));
    font-family: "Montserrat", sans-serif;
    position: relative;
  }
  .card {
    position: absolute;
    left: 270px;
    width: 660px;
    height: 378px;
    box-shadow: 0 10px 24px rgba(0,0,0,.35);
    overflow: hidden;
  }

  /* Back of card */
  .card--back { top: 50px; background: var(--card-dark); color: #fff; }
  .back__brand {
    position: absolute; top: 38px; left: 0; right: 0; text-align: center;
    font-family: "Exo 2", sans-serif; font-weight: 700; font-size: 34px;
    letter-spacing: 2px; text-transform: uppercase; color: var(--muted);
  }
  .back__heading {
    position: absolute; top: 110px; left: 40px; right: 40px;
    display: flex; align-items: center; gap: 14px;
  }
  .back__heading::before, .back__heading::after {
    content: ""; flex: 1; height: 1px; background: var(--rule);
  }
  .back__heading h2 { font-size: 17px; font-weight: 700; letter-spacing: .5px; }
  .services {
    position: absolute; top: 144px; left: 0; right: 0; text-align: center;
    font-size: 13px; font-weight: 500; line-height: 1.6; list-style: none;
  }
  .services li { display: inline; }
  .services li + li::before { content: "•"; color: var(--brand-red); margin: 0 8px; }
  .services .break { display: block; height: 0; }
  .appointment {
    position: absolute; top: 226px; left: 0; right: 0; height: 112px;
    background: var(--card-white); padding: 22px 40px;
    display: flex; flex-direction: column; justify-content: space-around;
  }
  .appointment__row { display: flex; align-items: flex-end; gap: 8px; }
  .appointment__label { color: var(--brand-red); font-size: 14px; font-weight: 500; }
  .appointment__line { flex: 1; border-bottom: 2px dotted #444; height: 1px; margin-bottom: 4px; }
  .appointment__line--date { flex: 1.3; }

  /* Front of card */
  .card--front { top: 472px; background: var(--card-white); color: var(--ink); }
  .front__brand {
    position: absolute; top: 36px; left: 40px;
    font-family: "Exo 2", sans-serif; font-weight: 700; font-size: 24px;
    letter-spacing: 1.5px; text-transform: uppercase; color: var(--brand-red);
  }
  .contact {
    position: absolute; left: 40px; top: 196px;
    font-family: "Exo 2", sans-serif; font-size: 15px; color: #333; font-style: normal;
  }
  .contact__address { line-height: 1.3; margin-bottom: 8px; font-size: 16px; }
  .contact__list { list-style: none; }
  .contact__list li { display: flex; align-items: center; gap: 8px; line-height: 1.5; }
  .contact__list .num { font-size: 16px; }
  .contact__list svg { width: 13px; height: 13px; flex: none; fill: var(--brand-red); }
  .name-band {
    position: absolute; right: 0; bottom: 42px; width: 330px; height: 84px;
    background: var(--band-black);
    clip-path: polygon(44px 0, 100% 0, 100% 100%, 0 100%);
    text-align: right; padding: 10px 28px 0 0;
    font-family: "Bebas Neue", sans-serif;
  }
  .name-band__name { color: var(--brand-red); font-size: 40px; line-height: 1; font-weight: 400; }
  .name-band__role { color: #fff; font-size: 26px; line-height: 1; }
</style>
</head>
<body>

<section class="card card--back" aria-label="Business card back">
  <p class="back__brand">Ridgeback Prime Automotive</p>
  <div class="back__heading"><h2>VEHICLE SERVICING</h2></div>
  <ul class="services">
    <li>All Mechanical Repairs</li><li>Warrant of Fitness</li><li>Tyres &amp; Wheel Alignments</li>
    <span class="break"></span>
    <li style="margin:0">Automotive Diagnostics</li><li>Automotive Parts &amp; Supplies</li>
  </ul>
  <div class="appointment">
    <div class="appointment__row">
      <span class="appointment__label">Date:</span><span class="appointment__line appointment__line--date"></span>
      <span class="appointment__label">Time:</span><span class="appointment__line"></span>
    </div>
    <div class="appointment__row">
      <span class="appointment__label">Date:</span><span class="appointment__line appointment__line--date"></span>
      <span class="appointment__label">Time:</span><span class="appointment__line"></span>
    </div>
  </div>
</section>

<section class="card card--front" aria-label="Business card front">
  <p class="front__brand">Ridgeback Prime Automotive</p>
  <address class="contact">
    <p class="contact__address">48 Marlow Lane<br>Whitianga 3510</p>
    <ul class="contact__list">
      <li><svg viewBox="0 0 16 16" aria-hidden="true"><path d="M3.5 1 6 4 4.6 5.8a9 9 0 0 0 5.6 5.6L12 10l3 2.5-1.5 2.5C7 15 1 9 1 2.5Z"/></svg><span class="num">07 842 1937</span></li>
      <li><svg viewBox="0 0 16 16" aria-hidden="true"><path d="M4 1h8v14H4Zm1.5 1.5v9h5v-9Z"/></svg><span class="num">027 519 2764</span></li>
      <li><svg viewBox="0 0 16 16" aria-hidden="true"><path d="M1 3h14v10H1Zm1.5 1.5L8 9l5.5-4.5Z"/></svg><span>office@ridgebackmotors.co.nz</span></li>
      <li><svg viewBox="0 0 16 16" aria-hidden="true"><circle cx="8" cy="8" r="7"/></svg><span>www.ridgebackmotors.co.nz</span></li>
    </ul>
  </address>
  <div class="name-band">
    <p class="name-band__name">Lachie Westergaard</p>
    <p class="name-band__role">Director</p>
  </div>
</section>

</body>
</html>
```